Talvor GmbH business card

We Talvor GmbH based in Switzerland are looking for a business card design. The Fresh Jung, appealing to customers of all kinds. We already have a logo to upload but still a business card. Details: Talvor GmbH Address: Lindenweg 14b in 9476 Brugwil. Tel: 41 79 462 37 18, web: Talvor.ch, E-mail: info@Talvor.ch Facebook: Talvor GmbH. I am the Managing Director: Luka Petrovac. On reverse: Title: Transporter and bus rental Gross: Without deposit Super prices
Contact Information for Business Card
Siehe Projektbeschreibung
Requirements
Should not have
- Other pictures

```html
<!DOCTYPE html>
<html lang="de">
<head>
<meta charset="utf-8">
<title>Talvor GmbH – Visitenkarte</title>
<link rel="stylesheet" href="https://fonts.googleapis.com/css2?family=Montserrat:wght@500;600;700;800&display=swap">
<style>
  :root {
    --stage: #2a2a2c;
    --steel: #7f9cb8;
    --mid-blue: #4a6898;
    --navy: #252a6e;
    --ink: #1f2a6b;
    --sub: #8fa6c4;
    --paper: #ffffff;
    --ghost: #eef0f4;
  }
  * { margin: 0; padding: 0; box-sizing: border-box; }
  html, body {
    width: 1200px; height: 852px; overflow: hidden;
    background: var(--stage);
    font-family: "Montserrat", sans-serif;
  }
  .card {
    position: absolute;
    width: 600px; height: 343px;
    border-radius: 20px;
    overflow: hidden;
    box-shadow: 0 10px 30px rgba(0,0,0,.45);
  }
  .card-front { left: 110px; top: 60px; }
  .card-back { left: 490px; top: 440px; background: var(--paper); }
  .card svg.bands { position: absolute; inset: 0; width: 100%; height: 100%; }

  .front-brand {
    position: absolute; inset: 0;
    display: flex; align-items: center; justify-content: center; gap: 14px;
    color: var(--paper);
    font-weight: 800; font-size: 46px; letter-spacing: 1px;
  }
  .brand-square { width: 26px; height: 26px; background: var(--paper); }

  .ghost-square {
    position: absolute; right: 0; top: 0;
    width: 220px; height: 215px; background: var(--ghost);
  }
  .back-mark {
    position: absolute; right: 60px; top: 50px;
    display: flex; align-items: center; gap: 14px;
  }
  .mark-square { width: 34px; height: 34px; background: var(--navy); }
  .mark-name { color: var(--navy); font-weight: 800; font-size: 40px; }

  .person { position: absolute; left: 40px; top: 112px; padding-left: 12px; border-left: 5px solid var(--ink); }
  .person-name { color: var(--ink); font-weight: 700; font-size: 19px; text-transform: uppercase; line-height: 1.1; }
  .person-role { color: var(--sub); font-weight: 600; font-size: 13px; text-transform: uppercase; }

  .contacts { position: absolute; left: 40px; top: 196px; list-style: none; }
  .contacts li {
    display: flex; align-items: center; gap: 10px;
    color: var(--ink); font-weight: 600; font-size: 16px; line-height: 24px;
  }
  .contacts svg { width: 14px; height: 14px; fill: none; stroke: var(--mid-blue); stroke-width: 2; }

  .address {
    position: absolute; left: 110px; bottom: 14px;
    color: var(--paper); font-weight: 500; font-size: 13px;
  }
  .social {
    position: absolute; right: 26px; top: 268px;
    display: flex; align-items: center; gap: 8px;
    color: var(--paper); font-weight: 600; font-size: 13px;
  }
  .social-square { width: 14px; height: 14px; background: var(--paper); }
</style>
</head>
<body>
  <section class="card card-front" aria-label="Vorderseite">
    <svg class="bands" viewBox="0 0 600 343" preserveAspectRatio="none" aria-hidden="true">
      <rect width="600" height="343" fill="var(--steel)"/>
      <polygon points="400,0 600,0 600,343 140,343" fill="var(--mid-blue)"/>
      <polygon points="560,0 600,0 600,343 360,343" fill="var(--navy)"/>
    </svg>
    <div class="front-brand"><span class="brand-square"></span>Talvor GmbH</div>
  </section>

  <section class="card card-back" aria-label="Rückseite">
    <span class="ghost-square"></span>
    <svg class="bands" viewBox="0 0 600 343" preserveAspectRatio="none" aria-hidden="true">
      <polygon points="0,343 0,315 600,225 600,343" fill="var(--mid-blue)"/>
      <polygon points="30,343 60,306 420,252 350,343" fill="var(--navy)"/>
    </svg>
    <div class="back-mark">
      <span class="mark-square"></span>
      <span class="mark-name">Talvor</span>
    </div>
    <div class="person">
      <p class="person-name">Luka Petrovac</p>
      <p class="person-role">Manager</p>
    </div>
    <ul class="contacts">
      <li><svg viewBox="0 0 14 14"><path d="M3 1l2 3-1.5 1.5a8 8 0 0 0 5 5L10 9l3 2-1.5 2C6 13 1 8 1 2.5z"/></svg>+41-79-462-37 18</li>
      <li><svg viewBox="0 0 14 14"><rect x="1" y="2" width="12" height="8"/><path d="M5 13h4"/></svg>www.Talvor.ch</li>
      <li><svg viewBox="0 0 14 14"><rect x="1" y="3" width="12" height="8"/><path d="M1 3l6 5 6-5"/></svg>info@Talvor.ch</li>
    </ul>
    <p class="address">Lindenweg 14b in 9476 Brugwil</p>
    <div class="social"><span class="social-square"></span>Talvor GmbH</div>
  </section>
</body>
</html>
```